Real Estate Company Needs Stationery Design Project, Logo Redesign, For Sale Design

We are a real estate company in San Diego California. We handle mostly coastal areas with middle to high end properties. Our colors are gray, dark silver, and black. I do not want anything Cartoon-ish but it does need to have a modern feel. We are looking to have these items below designed. We have a logo that we like and we have already built some name recognition so I don’t want to change the design but I am open to it… so feel free to pitch a new logo if you would like. We do however need our logo designed by a pro and put into high resolution Illustrator file. We listed the items we need designed below 1-4 with a description of what we are looking for below that. We need items 1-4 done with item 5 being optional for you designers. I attached our logo, current business cards, and a picture of real estate for sale sings for reference. Please feel free to email us if you have an questions.

Needs:
1) Logo Redesign.
- I Attached the Logo. I made this logo and need it to be done by a pro.
- I need my logo to be done in high resolution and an illustrator file
- I also need a copy of the logo to fit as my Pagebook background: 851 Wide by 315px Tall

2) Business Cards
- I need business cards design in an illustrator file.
- I need cards designed once with a space for a personal photo and one designed without a personal photo. Personal Photo = A picture of the agent or person.

3) Real Estate For sale signs Designed.
- I need these signs to fit 24”x18”
- Do not say For Sale on them, just have info as listed below
- I would like one design with a space for a personal picture of me, and one designed without a space for a picture
- Need this in an illustrator file

4) Stationary items

5) Some optional items that we could use are:
- Email Signature
- Newsletter template design
- Background design for Chirpr page
- Header and footer. One without contact info and one with contact info
For sale Signs Need: Logo, My Name, 888 #, website.
I do not want them to say “For Sale” on them. I attached a picture of some example signs. I also wouldn’t mind for it to say something in small writing along the lines of “View this home at –or- view details of this home at: CoastlineHomesNowPortal.example”

Cards need: Logo, Name, Serving All San Diego County, Cell #, Office/Fax#, Email, Website, DRE Lic#.
Backside should have either Logo or say something like “Referrals are the largest complements we can get…” Basically be creative, we could even use it to list all of our social media platforms: Pagebook, Chirpr, Website, Vidtube, Blorp+.

What to Avoid: Comic / Cartoonish look, but needs to be modern and smooth.

Martin Kellowey
The Kellowey Group
Real Estate Sales & Investments
Covering All San Diego County “Optional”
Cell: 760-555-0193
Office/Fax 888-555-0142
Martin@KelloweyGroup.example
www.CoastlineHomesNowPortal.example
DRE#09372514

Social Media:
http://www.facebook.example/KelloweyGroup
http://www.youtube.example/KelloweyGroup
http://www.yelp.example/biz/the-kellowey-group-oceanside-2

Find us on:
Homvia.example
Parcelo.example
Estatly.example
Blorp+
WorkNexa.example

Target Market(s)

San Diego California Real Estate.

Industry/Entity Type

Real Estate

Requirements
Must have
• 1) Logo Redesign.

2) Business Cards

4) Stationary items
Nice to have
• 5) Some optional items that we could use are:
- Email Signature
Should not have
• Cartoon look.

```html
<!DOCTYPE html>
<html lang="en">
<head>
<meta charset="utf-8">
<title>The Kellowey Group – Stationery Set</title>
<link rel="stylesheet" href="https://fonts.googleapis.com/css2?family=Cinzel:wght@500&family=Didact+Gothic&family=Montserrat:wght@600&display=swap">
<style>
:root{
  --bg-center:#2b2b2b;
  --bg-edge:#070707;
  --ink-dark:#111;
  --panel-top:#3a3a3a;
  --panel-bottom:#121212;
  --silver-light:#f2f2f2;
  --silver-mid:#c9c9c9;
  --silver-dark:#8e8e8e;
  --paper:#ffffff;
  --text-light:#e8e8e8;
  --text-dark:#1a1a1a;
  --window:#e6e6e6;
}
*{margin:0;padding:0;box-sizing:border-box}
html,body{width:1200px;height:1000px;overflow:hidden}
body{
  position:relative;
  background:radial-gradient(ellipse at 50% 45%,var(--bg-center) 0%,var(--bg-edge) 80%);
  font-family:"Didact Gothic",sans-serif;
}
.piece{position:absolute;overflow:hidden;box-shadow:0 6px 18px rgba(0,0,0,.55)}
.dark{background:linear-gradient(180deg,var(--panel-top),var(--panel-bottom))}
.silver-band{position:absolute;left:0;right:0;background:linear-gradient(90deg,var(--silver-dark),var(--silver-light) 45%,var(--silver-mid) 70%,var(--silver-dark))}
.black-band{position:absolute;left:0;right:0;background:var(--ink-dark)}

/* brand name block */
.brand{position:absolute;text-align:center;white-space:nowrap}
.brand-name{font-family:"Cinzel",serif;font-weight:500;color:var(--silver-mid);letter-spacing:.5px;display:flex;align-items:center;justify-content:center;gap:6px}
.brand-name .mark{display:inline-block;width:.45em;height:.45em;background:var(--silver-mid)}
.brand-rule{height:1px;background:var(--silver-dark);margin:3px auto 3px}
.brand-tag{font-family:"Cinzel",serif;color:var(--silver-mid);letter-spacing:1px}
.on-silver .brand-name,.on-silver .brand-tag{color:#3b3b3b}
.on-silver .brand-name .mark{background:#3b3b3b}
.on-silver .brand-rule{background:#555}

.photo-slot{position:absolute;background:#000;border:1px solid #555;box-shadow:inset 0 0 0 3px #000,inset 0 0 0 4px #777}
.agent-name{position:absolute;font-family:"Montserrat",sans-serif;font-weight:600;color:var(--text-light)}
.motto{position:absolute;font-style:italic;color:var(--text-light);font-size:6px}
.contact{position:absolute;color:var(--text-light);line-height:1.5}
.contact.right{text-align:right}
.contact.dark-text{color:var(--text-dark)}

/* pieces */
.card-logo-dark{left:56px;top:172px;width:246px;height:140px}
.card-logo-silver{left:56px;top:379px;width:245px;height:141px;background:linear-gradient(100deg,#a9a9a9,#ececec 40%,#cfcfcf 65%,#9d9d9d)}
.card-vertical{left:363px;top:113px;width:141px;height:247px}
.card-horizontal{left:324px;top:379px;width:246px;height:141px}
.letterhead{left:541px;top:115px;width:600px;height:778px;background:var(--paper)}
.envelope{left:56px;top:572px;width:627px;height:250px;background:var(--paper)}
.env-window{position:absolute;left:29px;top:171px;width:236px;height:52px;border:1px solid #c4c4c4;border-radius:9px;background:var(--window)}
</style>
</head>
<body>

<!-- business card front, dark -->
<section class="piece card-logo-dark dark">
  <div class="black-band" style="top:0;height:18px;background:linear-gradient(90deg,#000,#1d1d1d)"></div>
  <div class="black-band" style="bottom:0;height:20px;background:linear-gradient(90deg,#000,#2a2a2a)"></div>
  <div class="brand" style="left:20px;width:206px;top:56px">
    <div class="brand-name" style="font-size:16px"><span class="mark"></span>The Kellowey Group</div>
    <div class="brand-rule" style="width:180px"></div>
    <div class="brand-tag" style="font-size:6px">Real Estate Sales &amp; Investments</div>
  </div>
</section>

<!-- business card front, silver -->
<section class="piece card-logo-silver on-silver">
  <div class="silver-band" style="top:14px;height:4px;background:#777"></div>
  <div class="silver-band" style="bottom:14px;height:4px;background:#777"></div>
  <div class="black-band" style="top:0;height:14px;background:linear-gradient(90deg,#555,#999,#666)"></div>
  <div class="black-band" style="bottom:0;height:14px;background:linear-gradient(90deg,#555,#999,#666)"></div>
  <div class="brand" style="left:20px;width:206px;top:56px">
    <div class="brand-name" style="font-size:16px"><span class="mark"></span>The Kellowey Group</div>
    <div class="brand-rule" style="width:180px"></div>
    <div class="brand-tag" style="font-size:6px">Real Estate Sales &amp; Investments</div>
  </div>
</section>

<!-- business card back, vertical with photo -->
<section class="piece card-vertical dark">
  <div class="black-band" style="top:0;height:50px;background:#0c0c0c"></div>
  <div class="silver-band" style="top:50px;height:2px"></div>
  <div class="brand" style="left:4px;width:133px;top:18px">
    <div class="brand-name" style="font-size:10px"><span class="mark"></span>The Kellowey Group</div>
    <div class="brand-rule" style="width:110px;margin:2px auto"></div>
    <div class="brand-tag" style="font-size:4px">Real Estate Sales &amp; Investments</div>
  </div>
  <div class="photo-slot" role="img" aria-label="Space for agent portrait photo" style="left:37px;top:69px;width:67px;height:73px"></div>
  <div class="agent-name" style="left:0;width:141px;text-align:center;top:149px;font-size:10px">Martin Kellowey</div>
  <div class="motto" style="left:0;width:141px;text-align:center;top:162px">"Serving all San Diego County"</div>
  <div class="contact" style="left:20px;top:180px;font-size:6.5px;width:110px">
    <div style="padding-left:43px">Cell&nbsp;&nbsp;&nbsp;760 555 0193</div>
    <div style="padding-left:19px">Office / Fax&nbsp;&nbsp;888 555 0142</div>
  </div>
  <div class="contact" style="left:23px;top:206px;font-size:5px">
    <div>Martin@KelloweyGroup.example</div>
    <div>www.CoastlineHomesNowPortal.example</div>
  </div>
  <div class="contact" style="left:0;width:141px;text-align:center;top:229px;font-size:5px">DRE#09372514</div>
</section>

<!-- business card back, horizontal with photo -->
<section class="piece card-horizontal dark">
  <div class="black-band" style="top:0;height:30px;background:#0c0c0c"></div>
  <div class="silver-band" style="top:30px;height:3px"></div>
  <div class="photo-slot" role="img" aria-label="Space for agent portrait photo" style="left:18px;top:21px;width:68px;height:75px"></div>
  <div class="agent-name" style="left:99px;top:44px;font-size:11px">Martin Kellowey</div>
  <div class="motto" style="left:99px;top:59px">"Serving all San Diego County"</div>
  <div class="contact" style="left:99px;top:74px;font-size:7px">
    <div style="padding-left:24px">Cell&nbsp;&nbsp;&nbsp;760 555 0193</div>
    <div>Office / Fax&nbsp;&nbsp;&nbsp;888 555 0142</div>
  </div>
  <div class="contact" style="left:99px;top:110px;font-size:6.5px;line-height:1.6">
    <div>Martin@KelloweyGroup.example</div>
    <div>www.CoastlineHomesNowPortal.example</div>
  </div>
  <div class="contact" style="left:24px;top:122px;font-size:6px">DRE#09372514</div>
</section>

<!-- letterhead -->
<section class="piece letterhead">
  <div class="dark" style="position:absolute;left:0;right:0;top:0;height:77px;background:linear-gradient(90deg,#0c0c0c,#1e1e1e 60%,#3a3a3a)"></div>
  <div class="silver-band" style="top:77px;height:10px"></div>
  <div class="brand" style="left:22px;width:190px;top:30px">
    <div class="brand-name" style="font-size:16px"><span class="mark"></span>The Kellowey Group</div>
    <div class="brand-rule" style="width:180px"></div>
    <div class="brand-tag" style="font-size:6px">Real Estate Sales &amp; Investments</div>
  </div>
  <div class="contact right dark-text" style="right:13px;top:696px;font-size:8px;line-height:1.45">
    <div>Cell&nbsp;&nbsp;&nbsp;760 555 0193</div>
    <div>Office / Fax&nbsp;&nbsp;&nbsp;888 555 0142</div>
    <div>Martin@KelloweyGroup.example</div>
    <div>www.CoastlineHomesNowPortal.example</div>
  </div>
  <div class="contact dark-text" style="left:239px;top:733px;font-size:8px">DRE#09372514</div>
  <div class="silver-band" style="top:750px;height:10px"></div>
  <div class="black-band" style="top:760px;height:18px;background:linear-gradient(90deg,#000,#2a2a2a 80%,#0a0a0a)"></div>
</section>

<!-- envelope -->
<section class="piece envelope">
  <div class="dark" style="position:absolute;left:0;right:0;top:0;height:76px;background:linear-gradient(90deg,#0c0c0c,#1e1e1e 60%,#3a3a3a)"></div>
  <div class="silver-band" style="top:76px;height:9px"></div>
  <div class="brand" style="left:27px;width:190px;top:30px">
    <div class="brand-name" style="font-size:16px"><span class="mark"></span>The Kellowey Group</div>
    <div class="brand-rule" style="width:180px"></div>
    <div class="brand-tag" style="font-size:6px">Real Estate Sales &amp; Investments</div>
  </div>
  <div class="env-window"></div>
  <div class="contact right dark-text" style="right:12px;top:216px;font-size:7px">www.CoastlineHomesNowPortal.example</div>
  <div class="black-band" style="bottom:0;height:14px"></div>
</section>

</body>
</html>
```